Book and Ebook Cover for my Upcoming Book

About the Book
------------------
I need a book, ebook and if possible audio cover design for my upcoming book - Lanterns & Tides. This is my first book and really looking for a great book cover. The book is about my story, living with Mental Health and how to reclaim control of your life.

Pressmarble
-----------
I am using pressmarble.example to self-publish my book so in case of any design-related questions you can just search info on their website.

I have an initial theme I am thinking for the design book cover which I have attached. You can use this as a starting point.

Idea for the theme
---------------------
I am thinking about a phoenix to represent rising from the ashes and rebirth. The phoenix motif will be continued throughout the interior pages of the book. I'd like the cover of the book to be minimal, white with gold lettering, and maybe incorporating wings? feel free to play around with the idea and up for suggestions.

If you can think of something along these lines and make it a lot better that would be great.

What I need
---------------
The book is complete and is Trim size is 6.14 x 9.21” (234 x 156mm). I would need-
1. Book Cover
2. Back & Spine Design
3. Source File
4. Ebook Cover
5. Need multiple revisions to get the best possible outcome
6. My name and book title should also on the front cover
7. The book title should be bigger size than the subtitle

If you can give me Audiobook cover, I would love that as well and can pay extra for it if needed.

I love this for the interior phoenix motif:
https://artbazaarhub.example/VelloStudioWorks/7720418-Painted-Firebird-Graphic-Pack#fullscreen

The only other actual book cover I found online that remotely relates to what I am looking for is this -
https://www.searchloop.example/url?sa=i&url=https%3A%2F%2Fshotgallery.example%2Fkorvath&psig=BxQmTr7LK2pNvW4ZsYeHd83QaPLJ&ust=1598415525610000&source=images&cd=vfe&ved=1HXdkRmQBvubDGrTLkxbWsTqYhpTGEgcDHRRRRRHdBBBBBBCE

Target Market(s)

Personal Development
Mental health

Requirements
Must have
• 1. Book Cover
2. Back & Spine Design
3. Source File
4. Ebook Cover
Nice to have
• Audiobook cover as I eventually will be releasing the audio version of the book

```html
<!DOCTYPE html>
<html lang="en">
<head>
<meta charset="utf-8">
<title>Lanterns &amp; Tides — Cover Wrap</title>
<link rel="stylesheet" href="https://fonts.googleapis.com/css2?family=Cinzel:wght@400;500;600&family=Roboto+Condensed:wght@400&family=Cormorant+Garamond:ital,wght@0,500;1,500&display=swap">
<style>
  :root {
    --stage: #2a2a2a;
    --paper: #ffffff;
    --paper-shade: #f3f3f3;
    --ink: #1e1e1e;
    --body-ink: #2b2b2b;
    --gold-dark: #7a5418;
    --gold: #b8892f;
    --gold-light: #e8c66e;
    --rule: #9a8a6a;
    --photo: #5e5e5e;
    --gold-grad: linear-gradient(100deg, #6f4a14 0%, #b98a2e 28%, #f0d27c 48%, #a77a26 70%, #6f4a14 100%);
  }
  * { box-sizing: border-box; margin: 0; padding: 0; }
  html, body { width: 1200px; height: 1200px; overflow: hidden; }
  body {
    background: var(--stage);
    display: flex; align-items: center; justify-content: center;
  }
  .cover-wrap { display: flex; height: 780px; box-shadow: 0 20px 50px rgba(0,0,0,.45); }

  .gold-text {
    background: var(--gold-grad);
    -webkit-background-clip: text; background-clip: text;
    color: transparent;
  }

  /* BACK COVER */
  .back-cover {
    width: 520px; background: var(--paper);
    padding: 62px 44px 40px;
    display: flex; flex-direction: column;
    font-family: "Roboto Condensed", Arial, sans-serif;
    color: var(--body-ink);
  }
  .back-title {
    font-family: "Cinzel", serif; font-weight: 500;
    font-size: 24px; text-align: center; letter-spacing: .5px;
    color: var(--gold-dark);
  }
  .back-title-rule {
    height: 1px; width: 300px; margin: 10px auto 20px;
    background: linear-gradient(90deg, transparent, var(--rule), transparent);
  }
  .blurb p { font-size: 13.4px; line-height: 1.36; text-align: justify; margin-bottom: 12px; }
  .back-divider { display: flex; align-items: center; gap: 10px; margin: 20px 0 18px; }
  .back-divider .rule { flex: 1; height: 1px; background: linear-gradient(90deg, transparent, var(--rule)); }
  .back-divider .rule.right { background: linear-gradient(90deg, var(--rule), transparent); }
  .phoenix-mini {
    width: 96px; height: 58px; border-radius: 50% 50% 40% 40%;
    background: radial-gradient(ellipse at 50% 45%, var(--gold-light), var(--gold) 55%, rgba(184,137,47,0) 75%);
  }
  .about-heading {
    font-family: "Cinzel", serif; font-weight: 500; font-size: 17px;
    color: var(--gold-dark); text-align: center; margin-left: 100px; margin-bottom: 4px;
  }
  .author-bio { font-size: 13.4px; line-height: 1.36; text-align: justify; }
  .author-photo { float: left; width: 84px; height: 100px; background: var(--photo); margin: -20px 12px 4px 0; }
  .publisher-mark {
    margin-top: auto; display: flex; align-items: center; gap: 6px;
    font-family: "Cinzel", serif; font-size: 11px; letter-spacing: 2px; color: var(--ink);
  }
  .publisher-mark .mark-square { width: 14px; height: 14px; border: 1px solid var(--ink); }

  /* SPINE */
  .spine {
    width: 48px;
    background: linear-gradient(90deg, var(--paper-shade), var(--paper) 40%, var(--paper-shade));
    display: flex; flex-direction: column; align-items: center;
    padding: 34px 0 22px;
    font-family: "Cinzel", serif;
  }
  .spine-title, .spine-author {
    writing-mode: vertical-rl; font-size: 17px; font-weight: 500; letter-spacing: 1px;
  }
  .spine-title { color: var(--ink); }
  .spine-author { margin-top: 90px; color: var(--gold-dark); }
  .spine .publisher-mark { writing-mode: vertical-rl; margin-top: auto; font-size: 9px; gap: 4px; }
  .spine .mark-square { width: 10px; height: 10px; }

  /* FRONT COVER */
  .front-cover {
    width: 520px; background: var(--paper);
    display: flex; flex-direction: column; align-items: center;
    padding-top: 56px; font-family: "Cinzel", serif;
  }
  .front-title { font-size: 72px; font-weight: 500; line-height: 1; letter-spacing: 1px; }
  .title-joiner { display: flex; align-items: center; gap: 14px; width: 390px; margin: 6px 0 8px; }
  .title-joiner .rule { flex: 1; height: 2px; background: linear-gradient(90deg, transparent, #8d8d8d); }
  .title-joiner .rule.right { background: linear-gradient(90deg, #8d8d8d, transparent); }
  .ampersand { font-family: "Cormorant Garamond", serif; font-size: 42px; line-height: 1; color: #8a8a8a; }
  .phoenix-art {
    width: 420px; height: 290px; margin-top: 30px;
    background: radial-gradient(ellipse 55% 50% at 50% 45%, var(--gold-light) 0%, var(--gold) 45%, rgba(184,137,47,.25) 72%, rgba(255,255,255,0) 80%);
  }
  .subtitle {
    margin-top: 40px; text-align: center;
    font-size: 21px; line-height: 1.3; letter-spacing: 1px; color: var(--ink);
  }
  .front-author { margin-top: 52px; font-size: 42px; font-weight: 500; letter-spacing: 1px; }
</style>
</head>
<body>
  <main class="cover-wrap">
    <section class="back-cover">
      <h2 class="back-title">Lanterns &amp; Tides</h2>
      <div class="back-title-rule"></div>
      <div class="blurb">
        <p>Lorem Ipsum is simply dummy text of the printing and typesetting industry. Lorem Ipsum has been the industry's standard dummy text ever since the 1500s, when an unknown printer took a galley of type and scrambled it to make a type specimen book. It has survived not only five centuries, but also the leap into electronic typesetting, remaining essentially unchanged. It was popularised in the 1960s with the release of Letraset sheets containing Lorem Ipsum passages, and more recently with desktop publishing software like Aldus PageMaker including versions of Lorem Ipsum.</p>
        <p>Lorem Ipsum is simply dummy text of the printing and typesetting industry. Lorem Ipsum has been the industry's standard dummy text ever since the 1500s, when an unknown printer took a galley of type and scrambled it to make a type specimen book. It has survived not only five centuries, but also the leap into electronic typesetting, remaining essentially unchanged.</p>
      </div>
      <div class="back-divider">
        <span class="rule"></span>
        <div class="phoenix-mini" role="img" aria-label="Small gold phoenix emblem with spread wings"></div>
        <span class="rule right"></span>
      </div>
      <h3 class="about-heading">About the Author</h3>
      <div class="author-bio">
        <div class="author-photo" role="img" aria-label="Author portrait photograph"></div>
        Lorem Ipsum is simply dummy text of the printing and typesetting industry. Lorem Ipsum has been the industry's standard dummy text ever since the 1500s, when an unknown printer took a galley of type and scrambled it to make a type specimen book. It has survived not only five centuries, but also Lorem Ipsum is simply dummy text of the printing and typesetting industry. Lorem Ipsum has been the industry's standard dummy text ever since the 1500s, when an unknown printer took a galley.
      </div>
      <div class="publisher-mark"><span class="mark-square"></span>TIDEWELL</div>
    </section>

    <section class="spine">
      <span class="spine-title">Lanterns &amp; Tides</span>
      <span class="spine-author">Maren Solvey</span>
      <div class="publisher-mark"><span class="mark-square"></span>TIDEWELL</div>
    </section>

    <section class="front-cover">
      <h1 class="front-title gold-text">LANTERNS</h1>
      <div class="title-joiner">
        <span class="rule"></span><span class="ampersand">&amp;</span><span class="rule right"></span>
      </div>
      <h1 class="front-title gold-text">TIDES</h1>
      <div class="phoenix-art" role="img" aria-label="Gold foil phoenix rising with wings spread wide"></div>
      <p class="subtitle">Reinvent your life<br>and own your story</p>
      <p class="front-author gold-text">MAREN SOLVEY</p>
    </section>
  </main>
</body>
</html>
```